mobile app design: app provides timely Natural gas pipeline information (similar to weather, etc)

we are going to create and publish an app in all the three markets.( android, ios,windows). we have wire framed mostly all the screens. the designers are to provide the layout, design & background. The following are the most important things.

1. the app's target audience are guys working in the natural gas industry in the US.
2. the app provides the customer with latest pipeline information
3. the trial version is free and will provide information about one pipeline
4. slides 1 to 5 are trial version slides.
5. slides 6 onwards the customer chooses.
6. the final product is displayed in a grid.
7. the app will be developed using html5 and css3.
8. customer will pay per pipeline for the information. ( in app payment)
9 there are similiar ( complementary) products which provide weekly storage data at vendra shelf and bramlo soft bazaar.
10. i have attached the pdf document of the wireframe.
11.i have attached the logo
12. no name has been thought out yet.

Hi guys

I have a main question for the designer community .

1. is it possible to combine some of the pages ( screens  ) into one or two. use your gut feel. if not it is ok.

2. check out the flow, the color, the background , the font and the font size. it should be pleasing.

thanx

Tomek

```html
<!DOCTYPE html>
<html lang="en">
<head>
<meta charset="utf-8">
<title>Pipelines app screens</title>
<link rel="stylesheet" href="https://fonts.googleapis.com/css2?family=Open+Sans:wght@400;600;700&display=swap">
<style>
:root{
  --page:#e8eef0;
  --teal:#22b2a6;
  --teal-light:#52c8be;
  --teal-dark:#1a9c91;
  --status:#2c2c2c;
  --bar:#333333;
  --content:#ebebeb;
  --white:#ffffff;
  --row-alt:#f6f6f6;
  --text:#444444;
  --muted:#8a8a8a;
  --line:#dddddd;
  --check-box:#f3f3f3;
}
*{box-sizing:border-box;margin:0;padding:0}
html,body{width:1200px;height:1057px;overflow:hidden}
body{background:var(--page);font-family:"Open Sans",Arial,sans-serif;color:var(--text);position:relative}
.screen{position:absolute;top:120px;width:460px;height:816px;background:var(--content);overflow:hidden;box-shadow:0 10px 30px rgba(0,0,0,.15)}
.screen--list{left:100px}
.screen--table{left:640px}
.status-bar{height:25px;background:var(--status);color:#fff;font-weight:700;font-size:16px;display:flex;align-items:center;justify-content:space-between;padding:0 6px;letter-spacing:.2px}
.status-left,.status-right{display:flex;align-items:center;gap:5px}
.title-bar{height:46px;background:linear-gradient(90deg,var(--teal),var(--teal-light));color:#fff;font-size:21px;text-align:center;line-height:44px;letter-spacing:-.3px}
.nav-bar{height:50px;background:var(--white);position:relative;font-size:11.5px;color:var(--muted)}
.nav-item{position:absolute;top:0;height:50px;display:flex;align-items:center;gap:10px}
.content{position:relative;height:695px}
.bottom-bar{position:absolute;left:0;bottom:0;width:100%;height:57px;background:var(--bar)}
.bottom-bar svg{position:absolute;top:18px}
/* list screen */
.pipeline-list{position:absolute;left:0;top:42px;width:100%;list-style:none}
.pipeline{height:33px;position:relative;font-size:12.5px;display:flex;align-items:center}
.pipeline::before{content:"";position:absolute;left:85px;width:318px;height:20px;top:6px}
.pipeline:nth-child(odd)::before{background:var(--white)}
.pipeline .box{position:absolute;left:51px;top:8px;width:17px;height:16px;border-radius:3px;background:var(--check-box)}
.pipeline .tick{position:absolute;left:50px;top:5px}
.pipeline .name{position:relative;margin-left:96px;letter-spacing:-.2px}
.scroll{position:absolute;width:5px;border-radius:3px;background:#dedede}
.scroll span{display:block;width:100%;height:60px;border-radius:3px;background:#f8f8f8}
.next-button{position:absolute;left:180px;top:530px;width:84px;height:84px;border-radius:50%;background:#cfcfcf;border:2px solid #dcdcdc;display:flex;align-items:center;justify-content:center}
/* table screen */
.data-table{position:absolute;left:15px;top:25px;width:417px;border-collapse:collapse;font-size:12px;table-layout:fixed}
.data-table th{height:41px;background:linear-gradient(90deg,var(--teal) 0%,var(--teal) 60%,var(--teal-dark) 62%,var(--teal-light) 100%);color:#fff;font-weight:700;font-size:12.5px}
.data-table td{height:37px;text-align:center;background:var(--white)}
.data-table tr:nth-child(even) td{background:var(--row-alt)}
.data-table td.date{font-size:8.5px;border-left:1px solid var(--line);color:#666}
.table-actions{position:absolute;left:78px;top:568px;width:304px;height:41px;display:flex;border-radius:4px;overflow:hidden;border:1px solid #d4d4d4;font-size:13.5px}
.action{flex:1;display:flex;align-items:center;justify-content:center;background:var(--white);color:var(--text)}
.action--primary{background:var(--teal);color:#fff}
</style>
</head>
<body>

<!-- Pipeline selection screen -->
<section class="screen screen--list">
  <div class="status-bar">
    <div class="status-left">
      <svg width="26" height="12" viewBox="0 0 26 12"><rect x="0" y="8" width="3" height="4" fill="#fff"/><rect x="5" y="6" width="3" height="6" fill="#fff"/><rect x="10" y="4" width="3" height="8" fill="#fff"/><rect x="15" y="2" width="3" height="10" fill="#fff"/><rect x="20" y="0" width="3" height="12" fill="#fff"/></svg>
      <span>VOLT</span>
    </div>
    <span>10:35 AM</span>
    <div class="status-right">
      <svg width="13" height="13" viewBox="0 0 13 13"><circle cx="6.5" cy="6.5" r="6" fill="#fff"/><path d="M6.5 3v3.5H4" stroke="#2c2c2c" stroke-width="1.5" fill="none"/></svg>
      <span>65%</span>
      <svg width="28" height="13" viewBox="0 0 28 13"><rect x="0.5" y="0.5" width="24" height="12" fill="none" stroke="#fff"/><rect x="2" y="2" width="14" height="9" fill="#fff"/><rect x="25" y="4" width="2" height="5" fill="#fff"/></svg>
    </div>
  </div>
  <header class="title-bar">Pipelines</header>
  <nav class="nav-bar">
    <div class="nav-item" style="left:30px">
      <svg width="20" height="17" viewBox="0 0 20 17"><rect y="0" width="20" height="3" fill="var(--teal)"/><rect y="7" width="20" height="3" fill="var(--teal)"/><rect y="14" width="20" height="3" fill="var(--teal)"/></svg>
      <span>Main Menu</span>
    </div>
    <div class="nav-item" style="left:186px">
      <svg width="22" height="22" viewBox="0 0 22 22"><circle cx="11" cy="11" r="11" fill="var(--teal)"/><text x="11" y="16" text-anchor="middle" font-family="Open Sans,sans-serif" font-weight="700" font-size="14" fill="#fff">$</text></svg>
      <span>Payment</span>
    </div>
    <div class="nav-item" style="left:322px">
      <svg width="22" height="22" viewBox="0 0 22 22"><circle cx="11" cy="11" r="9.5" fill="none" stroke="var(--teal)" stroke-width="2"/><path d="M16 11H7M10.5 7L6.5 11l4 4" stroke="var(--teal)" stroke-width="2" fill="none"/></svg>
      <span>To Trial version</span>
    </div>
  </nav>
  <main class="content">
    <ul class="pipeline-list">
      <li class="pipeline"><svg class="tick" width="22" height="18" viewBox="0 0 22 18"><path d="M2 9l6 6L20 3" stroke="var(--teal)" stroke-width="2.5" fill="none"/></svg><span class="name">Quillmark Pipeline Company</span></li>
      <li class="pipeline"><span class="box"></span><span class="name">Ridgeline Express Pipeline</span></li>
      <li class="pipeline"><span class="box"></span><span class="name">Rowan Pipeline</span></li>
      <li class="pipeline"><span class="box"></span><span class="name">Sable Trails Pipeline</span></li>
      <li class="pipeline"><span class="box"></span><span class="name">Sundale Natural Gas Company</span></li>
      <li class="pipeline"><svg class="tick" width="22" height="18" viewBox="0 0 22 18"><path d="M2 9l6 6L20 3" stroke="var(--teal)" stroke-width="2.5" fill="none"/></svg><span class="name">Silverstar Central Gas Pipeline, Inc</span></li>
      <li class="pipeline"><span class="box"></span><span class="name">Sunvale</span></li>
      <li class="pipeline"><svg class="tick" width="22" height="18" viewBox="0 0 22 18"><path d="M2 9l6 6L20 3" stroke="var(--teal)" stroke-width="2.5" fill="none"/></svg><span class="name">Tallbrook Gas Pipeline Company</span></li>
      <li class="pipeline"><span class="box"></span><span class="name">Tarrow Eastern Transmission Pipeline</span></li>
      <li class="pipeline"><span class="box"></span><span class="name">Tamsin Gas Pipe Line Corporation</span></li>
      <li class="pipeline"><svg class="tick" width="22" height="18" viewBox="0 0 22 18"><path d="M2 9l6 6L20 3" stroke="var(--teal)" stroke-width="2.5" fill="none"/></svg><span class="name">Tolland Gas Transmission, LLC [7]</span></li>
      <li class="pipeline"><span class="box"></span><span class="name">Tessel-Orin Pipeline</span></li>
      <li class="pipeline"><span class="box"></span><span class="name">Trailwick Pipeline Company</span></li>
      <li class="pipeline"><span class="box"></span><span class="name">Transmeridian Pipeline</span></li>
    </ul>
    <div class="scroll" style="left:420px;top:40px;height:444px"><span></span></div>
    <div class="next-button">
      <svg width="50" height="50" viewBox="0 0 50 50"><circle cx="25" cy="25" r="21" fill="none" stroke="#fff" stroke-width="3.5"/><path d="M13 25h22M26 15l10 10-10 10" stroke="#fff" stroke-width="3.5" fill="none"/></svg>
    </div>
    <footer class="bottom-bar">
      <svg style="left:75px" width="20" height="18" viewBox="0 0 20 18"><rect y="1" width="20" height="2.5" fill="#ccc"/><rect y="8" width="20" height="2.5" fill="#ccc"/><rect y="15" width="20" height="2.5" fill="#ccc"/></svg>
      <svg style="left:208px" width="22" height="22" viewBox="0 0 22 22"><circle cx="11" cy="11" r="11" fill="#ccc"/><text x="11" y="16" text-anchor="middle" font-family="Open Sans,sans-serif" font-weight="700" font-size="14" fill="#333">$</text></svg>
      <svg style="left:355px" width="22" height="22" viewBox="0 0 22 22"><circle cx="11" cy="11" r="9.5" fill="none" stroke="#ccc" stroke-width="2"/><path d="M16 11H7M10.5 7L6.5 11l4 4" stroke="#ccc" stroke-width="2" fill="none"/></svg>
    </footer>
  </main>
</section>

<!-- Pipeline grid screen -->
<section class="screen screen--table">
  <div class="status-bar">
    <div class="status-left">
      <svg width="26" height="12" viewBox="0 0 26 12"><rect x="0" y="8" width="3" height="4" fill="#fff"/><rect x="5" y="6" width="3" height="6" fill="#fff"/><rect x="10" y="4" width="3" height="8" fill="#fff"/><rect x="15" y="2" width="3" height="10" fill="#fff"/><rect x="20" y="0" width="3" height="12" fill="#fff"/></svg>
      <span>VOLT</span>
    </div>
    <span>10:35 AM</span>
    <div class="status-right">
      <svg width="13" height="13" viewBox="0 0 13 13"><circle cx="6.5" cy="6.5" r="6" fill="#fff"/><path d="M6.5 3v3.5H4" stroke="#2c2c2c" stroke-width="1.5" fill="none"/></svg>
      <span>65%</span>
      <svg width="28" height="13" viewBox="0 0 28 13"><rect x="0.5" y="0.5" width="24" height="12" fill="none" stroke="#fff"/><rect x="2" y="2" width="14" height="9" fill="#fff"/><rect x="25" y="4" width="2" height="5" fill="#fff"/></svg>
    </div>
  </div>
  <header class="title-bar">Add Pipelines</header>
  <nav class="nav-bar">
    <div class="nav-item" style="left:30px">
      <svg width="20" height="17" viewBox="0 0 20 17"><rect y="0" width="20" height="3" fill="var(--teal)"/><rect y="7" width="20" height="3" fill="var(--teal)"/><rect y="14" width="20" height="3" fill="var(--teal)"/></svg>
      <span>Main Menu</span>
    </div>
    <div class="nav-item" style="left:186px">
      <svg width="22" height="22" viewBox="0 0 22 22"><circle cx="11" cy="11" r="11" fill="var(--teal)"/><text x="11" y="16" text-anchor="middle" font-family="Open Sans,sans-serif" font-weight="700" font-size="14" fill="#fff">$</text></svg>
      <span>Payment</span>
    </div>
    <div class="nav-item" style="left:322px">
      <svg width="22" height="22" viewBox="0 0 22 22"><circle cx="11" cy="11" r="9.5" fill="none" stroke="var(--teal)" stroke-width="2"/><path d="M16 11H7M10.5 7L6.5 11l4 4" stroke="var(--teal)" stroke-width="2" fill="none"/></svg>
      <span>To Trial version</span>
    </div>
  </nav>
  <main class="content">
    <table class="data-table">
      <colgroup><col style="width:117px"><col style="width:113px"><col style="width:105px"><col style="width:82px"></colgroup>
      <thead><tr><th>Region</th><th>Pipeline</th><th>GasDay</th><th>Date</th></tr></thead>
      <tbody>
        <tr><td>Northwest</td><td>Tessel - Orin</td><td>Data</td><td class="date">May 15, 2014</td></tr>
        <tr><td>Northwest</td><td>Tessel - Orin</td><td>Data</td><td class="date">May 15, 2014</td></tr>
        <tr><td>Northwest</td><td>Tessel - Orin</td><td>Data</td><td class="date">May 15, 2014</td></tr>
        <tr><td>Northwest</td><td>Tessel - Orin</td><td>Data</td><td class="date">May 15, 2014</td></tr>
        <tr><td>Northwest</td><td>Tessel - Orin</td><td>Data</td><td class="date">May 15, 2014</td></tr>
        <tr><td>Northwest</td><td>Tessel - Orin</td><td>Data</td><td class="date">May 15, 2014</td></tr>
        <tr><td>Northwest</td><td>Tessel - Orin</td><td>Data</td><td class="date">May 15, 2014</td></tr>
        <tr><td>Northwest</td><td>Tessel - Orin</td><td>Data</td><td class="date">May 15, 2014</td></tr>
        <tr><td>Northwest</td><td>Tessel - Orin</td><td>Data</td><td class="date">May 15, 2014</td></tr>
        <tr><td>Northwest</td><td>Tessel - Orin</td><td>Data</td><td class="date">May 15, 2014</td></tr>
        <tr><td>Northwest</td><td>Tessel - Orin</td><td>Data</td><td class="date">May 15, 2014</td></tr>
        <tr><td>Northwest</td><td>Tessel - Orin</td><td>Data</td><td class="date">May 15, 2014</td></tr>
        <tr><td>Northwest</td><td>Tessel - Orin</td><td>Data</td><td class="date">May 15, 2014</td></tr>
      </tbody>
    </table>
    <div class="scroll" style="left:441px;top:78px;height:440px;width:4px"><span style="height:60px"></span></div>
    <div class="table-actions">
      <div class="action action--primary">Add Pipelines</div>
      <div class="action">Delete Pipelines</div>
    </div>
    <footer class="bottom-bar">
      <svg style="left:75px" width="20" height="18" viewBox="0 0 20 18"><rect y="1" width="20" height="2.5" fill="#ccc"/><rect y="8" width="20" height="2.5" fill="#ccc"/><rect y="15" width="20" height="2.5" fill="#ccc"/></svg>
      <svg style="left:208px" width="22" height="22" viewBox="0 0 22 22"><circle cx="11" cy="11" r="11" fill="#ccc"/><text x="11" y="16" text-anchor="middle" font-family="Open Sans,sans-serif" font-weight="700" font-size="14" fill="#333">$</text></svg>
      <svg style="left:355px" width="22" height="22" viewBox="0 0 22 22"><circle cx="11" cy="11" r="9.5" fill="none" stroke="#ccc" stroke-width="2"/><path d="M16 11H7M10.5 7L6.5 11l4 4" stroke="#ccc" stroke-width="2" fill="none"/></svg>
    </footer>
  </main>
</section>

</body>
</html>
```